Plumber needs a business card

I need a new business card for my plumbing business. I dont have a logo at the moment but I want business cards that are simple but very professional. I want to look like
Name: Mitch Dorley
Address: (just make one up)
Phone: 0455 318 726
Email: mitch@dorleymail.com
Colors to use:
Blacks, blues, silvers

```html
<!DOCTYPE html>
<html lang="en">
<head>
<meta charset="UTF-8">
<title>Mitch Dorley – Business Card</title>
<link rel="stylesheet" href="https://fonts.googleapis.com/css2?family=PT+Sans+Narrow:wght@700&display=swap">
<style>
  :root {
    --card-bg: #313a3d;
    --ink-white: #ffffff;
    --ink-silver: #dfe4e5;
    --accent-teal: #2a8fa5;
    --tool-blue: #1e6f88;
    --pipe-silver: #8a9a9a;
  }
  html, body {
    margin: 0;
    padding: 0;
    width: 1200px;
    height: 702px;
    overflow: hidden;
    background: var(--card-bg);
  }
  .card {
    position: relative;
    width: 1200px;
    height: 702px;
    background: var(--card-bg);
    font-family: "PT Sans Narrow", "Arial Narrow", sans-serif;
    font-weight: 700;
    overflow: hidden;
  }
  .tool-artwork {
    position: absolute;
    left: 0;
    top: 0;
    width: 650px;
    height: 702px;
    background:
      radial-gradient(ellipse at 22% 62%, rgba(30,111,136,0.85) 0%, rgba(30,111,136,0.35) 38%, rgba(49,58,61,0) 70%),
      linear-gradient(100deg, rgba(138,154,154,0) 55%, rgba(138,154,154,0.22) 68%, rgba(49,58,61,0) 82%);
  }
  .owner-name {
    position: absolute;
    right: 112px;
    top: 88px;
    margin: 0;
    font-size: 80px;
    line-height: 1;
    color: var(--ink-white);
    letter-spacing: 0.5px;
  }
  .contact-item {
    position: absolute;
    margin: 0;
    font-size: 33px;
    line-height: 47px;
    color: var(--ink-silver);
    text-align: right;
    white-space: nowrap;
  }
  .contact-address { top: 370px; right: 110px; }
  .contact-phone { top: 480px; right: 116px; }
  .contact-email { top: 544px; right: 116px; }
  .contact-icon {
    position: absolute;
    fill: var(--accent-teal);
  }
  .icon-pin { left: 772px; top: 377px; }
  .icon-phone { left: 777px; top: 491px; }
  .icon-mail { left: 772px; top: 559px; fill: none; stroke: var(--accent-teal); stroke-width: 1.6; }
</style>
</head>
<body>
  <div class="card">
    <div class="tool-artwork" role="img" aria-label="Illustration of a blue pipe wrench gripping silver plumbing pipes"></div>

    <h1 class="owner-name">Mitch Dorley</h1>

    <svg class="contact-icon icon-pin" width="22" height="32" viewBox="0 0 22 32" aria-hidden="true">
      <path d="M11 0C4.9 0 0 4.9 0 11c0 8 11 21 11 21s11-13 11-21C22 4.9 17.1 0 11 0zm0 15.5a4.5 4.5 0 1 1 0-9 4.5 4.5 0 0 1 0 9z"/>
    </svg>
    <p class="contact-item contact-address">418 Calder Street<br>Brookvale, CA 94120</p>

    <svg class="contact-icon icon-phone" width="14" height="24" viewBox="0 0 14 24" aria-hidden="true">
      <path d="M3 1h4l1 6-3 1.5c0 3 .5 5.5 2 7.5L10 15l3 5-3 3C5 23 1 16 1 10 1 5 2 2 3 1z"/>
    </svg>
    <p class="contact-item contact-phone">0455 318 726</p>

    <svg class="contact-icon icon-mail" width="24" height="18" viewBox="0 0 24 18" aria-hidden="true">
      <rect x="1" y="1" width="22" height="16"/>
      <path d="M1 1l11 9 11-9M1 17l8-7M23 17l-8-7"/>
    </svg>
    <p class="contact-item contact-email">mitch@dorleymail.com</p>
  </div>
</body>
</html>
```